Halloway Crest Backers Guild business cards

Create a single-sided business card for the Halloway Crest Backers Guild based on the attached logo.
The additional data fields include Name, Title, Email, Phone, and website.
Please use the following as sample data:
Name: Dean Varrow
Title: Co-Founder / Investor
Email: deanvarrow@mailtern.net
Phone: 555-314-2706
Website: www.hcbackersguild.com

Target Market(s)

Start ups, entrepreneurs, venture capitalists

Industry/Entity Type

Investment

Contact Information for Business Card

Professional business card. Technology company.

Font styles to use
Serif
Sans Serif

Requirements
Must have
• Include the HCBG logo (attached)
• Name
• Title
• Email
• Phone
• Website
Should not have
• Cute, cartoony

```html
<!DOCTYPE html>
<html lang="en">
<head>
<meta charset="utf-8">
<title>Halloway Crest Backers Guild – Business Card</title>
<link rel="stylesheet" href="https://fonts.googleapis.com/css2?family=Open+Sans:wght@400;700&family=Arimo:wght@400;700&display=swap">
<style>
  :root {
    --backdrop: #2e2e2e;
    --card: #fbfbfb;
    --green: #0f8f4c;
    --ink: #2a2a2a;
    --ink-soft: #1e1e1e;
  }
  * { box-sizing: border-box; margin: 0; padding: 0; }
  html, body {
    width: 1200px;
    height: 997px;
    overflow: hidden;
    background: var(--backdrop);
  }
  .card {
    position: absolute;
    left: 150px;
    top: 241px;
    width: 900px;
    height: 515px;
    background: var(--card);
    overflow: hidden;
    font-family: "Arimo", Arial, sans-serif;
    color: var(--ink-soft);
  }
  .card__band {
    position: absolute;
    left: 0; right: 0; bottom: 0;
    height: 20px;
    background: var(--green);
  }
  .brand__mark {
    position: absolute;
    left: 176px;
    top: 112px;
    width: 96px;
    height: 96px;
    border-radius: 50%;
    background: var(--green);
  }
  .brand__divider {
    position: absolute;
    left: 304px;
    top: 88px;
    width: 2px;
    height: 146px;
    background: var(--green);
  }
  .brand__name {
    position: absolute;
    left: 326px;
    top: 104px;
    font-family: "Open Sans", sans-serif;
    font-weight: 700;
    font-size: 30px;
    line-height: 36px;
    color: var(--ink);
    text-transform: uppercase;
    letter-spacing: 0.5px;
  }
  .rule {
    position: absolute;
    height: 2px;
    background: var(--green);
  }
  .rule--brand { left: 304px; top: 196px; width: 520px; }
  .rule--person { left: 40px; top: 318px; width: 300px; }
  .person {
    position: absolute;
    left: 340px;
    top: 262px;
    width: 260px;
    text-align: center;
  }
  .person__name {
    font-weight: 700;
    font-size: 27px;
    color: var(--green);
    letter-spacing: 0.5px;
    text-transform: uppercase;
  }
  .person__title {
    margin-top: 4px;
    font-size: 15px;
    text-transform: uppercase;
    letter-spacing: 0.3px;
  }
  .icons {
    position: absolute;
    left: 398px;
    top: 350px;
    display: flex;
    gap: 20px;
  }
  .icons svg { width: 28px; height: 28px; display: block; }
  .contact {
    position: absolute;
    left: 300px;
    top: 396px;
    width: 340px;
    text-align: center;
  }
  .contact__line { font-size: 19px; line-height: 28px; }
  .contact__line--web {
    font-weight: 700;
    color: var(--green);
    font-size: 20px;
  }
</style>
</head>
<body>
  <main class="card">
    <div class="brand__mark"></div>
    <div class="brand__divider"></div>
    <div class="brand__name">Halloway Crest<br>Backers Guild</div>
    <div class="rule rule--brand"></div>

    <div class="rule rule--person"></div>
    <div class="person">
      <div class="person__name">Dean Varrow</div>
      <div class="person__title">Co-Founder &amp; Investor</div>
    </div>

    <div class="icons">
      <svg viewBox="0 0 28 28" aria-label="Phone">
        <circle cx="14" cy="14" r="14" fill="#0f8f4c"/>
        <path d="M10.5 8c.6 0 1.8 2.6 1.5 3.2l-1 1c.7 1.6 2 2.9 3.6 3.6l1-1c.6-.3 3.2.9 3.2 1.5v1.6c0 .6-.5 1.1-1.1 1.1C12.5 19 9 15.5 9 10.3c0-.6.5-1.1 1.1-1.1z" fill="#fff" transform="translate(0 -1)"/>
      </svg>
      <svg viewBox="0 0 28 28" aria-label="Email">
        <circle cx="14" cy="14" r="14" fill="#0f8f4c"/>
        <rect x="8" y="9.5" width="12" height="9" rx="1" fill="#fff"/>
        <path d="M8.5 10l5.5 4.5 5.5-4.5" fill="none" stroke="#0f8f4c" stroke-width="1.2"/>
      </svg>
      <svg viewBox="0 0 28 28" aria-label="Website">
        <circle cx="14" cy="14" r="14" fill="#0f8f4c"/>
        <g fill="none" stroke="#fff" stroke-width="1.8" stroke-linecap="round">
          <path d="M12.5 15.5l3-3"/>
          <path d="M11.5 13.5l-1.8 1.8a2 2 0 0 0 2.9 2.9l1.8-1.8"/>
          <path d="M16.5 14.5l1.8-1.8a2 2 0 0 0-2.9-2.9l-1.8 1.8"/>
        </g>
      </svg>
    </div>

    <div class="contact">
      <div class="contact__line">555-314-2706</div>
      <div class="contact__line">deanvarrow@mailtern.net</div>
      <div class="contact__line contact__line--web">www.hcbackersguild.com</div>
    </div>

    <div class="card__band"></div>
  </main>
</body>
</html>
```